GPS Tracker Business Card Design

We need a business card for a GPS Vehicle tracking company. We sell the hardware for the vehicle and the software platform to monitor your vehicle/s. Including high asset non-powered vehicles like a trailer using our solar powered unit.
We like using dark blue to different shades of blue along with gold. We have phone apps for Android and Apple devices.

We have a platform for families wanting to track their teenage driver and children; Plus a Fleet vehicle tracking platform.

Features: unlimited number of vehicles and/or assets including snow mobiles forklifts generators trailers airport equipment

Reports for driving behavior reports and alerts dashboard fleet maintenace timeline view and replay geofence real time alerts logbook scheduling route optimization accounting integration fleet grouping closest vehicle locator On Board Diagnostics.

Benefits: Increased productivity improved fuel efficiency organizing your business improve time management simplify back end processes, reduce fleet fuel efficiency and expenses increase fleet security etc..

Please view website: Velmora.com

Industry/Entity Type

Business

Contact Information for Business Card

Harold B Pennick

```html
<!DOCTYPE html>
<html lang="en">
<head>
<meta charset="utf-8">
<title>Velmora Business Card</title>
<link rel="stylesheet" href="https://fonts.googleapis.com/css2?family=Montserrat:wght@300;400;500&display=swap">
<style>
  :root {
    --backdrop: #2b2c2e;
    --card: #1f2227;
    --ink: #f4f5f7;
    --muted: #8a8d92;
    --accent: #1a5fc4;
  }
  * { margin: 0; padding: 0; box-sizing: border-box; }
  html, body { width: 1200px; height: 1189px; overflow: hidden; }
  body {
    background: var(--backdrop);
    font-family: "Montserrat", Arial, sans-serif;
    color: var(--ink);
    position: relative;
  }
  .card {
    position: absolute;
    left: 150px;
    width: 900px;
    height: 514px;
    background: var(--card);
    border-radius: 28px;
    box-shadow: 0 18px 40px rgba(0,0,0,.45);
  }
  .card--front { top: 50px; }
  .card--back { top: 620px; }

  .brand { position: absolute; }
  .brand__name {
    font-weight: 300;
    color: var(--ink);
    letter-spacing: -1px;
    line-height: 1;
    white-space: nowrap;
  }
  .brand__tagline {
    font-weight: 400;
    color: var(--muted);
    text-align: right;
    letter-spacing: 1px;
    line-height: 1;
    white-space: nowrap;
  }

  .card--front .brand { left: 50%; transform: translateX(-50%); top: 150px; }
  .card--front .brand__name { font-size: 118px; }
  .card--front .brand__tagline { font-size: 28px; margin-top: 10px; }
  .card--front .website {
    position: absolute; left: 0; right: 0; top: 365px;
    text-align: center; font-size: 25px; letter-spacing: 1px;
  }

  .card--back .brand { left: 56px; top: 70px; }
  .card--back .brand__name { font-size: 104px; }
  .card--back .brand__tagline { font-size: 26px; margin-top: 8px; }

  .social { position: absolute; right: 60px; top: 52px; display: flex; gap: 16px; }
  .social__tile { width: 42px; height: 34px; background: var(--accent); border-radius: 3px; }

  .divider { position: absolute; left: 56px; top: 300px; width: 620px; height: 3px; background: var(--accent); }

  .person { position: absolute; right: 56px; top: 246px; text-align: right; }
  .person__name { font-size: 36px; font-weight: 400; letter-spacing: 1px; }
  .person__role { font-size: 26px; color: var(--accent); margin-top: 10px; letter-spacing: 1px; }

  .contacts { position: absolute; left: 56px; top: 365px; list-style: none; }
  .contacts__item { display: flex; align-items: center; gap: 16px; height: 40px; font-size: 28px; letter-spacing: 1px; }
  .contacts__icon { width: 30px; height: 30px; background: var(--accent); border-radius: 5px; display: flex; align-items: center; justify-content: center; }
  .contacts__icon svg { width: 20px; height: 20px; }

  .address { position: absolute; right: 56px; top: 372px; text-align: right; font-size: 27px; line-height: 1.35; letter-spacing: 1px; }
</style>
</head>
<body>

<section class="card card--front">
  <div class="brand">
    <div class="brand__name">Velmora</div>
    <div class="brand__tagline">Always Know Where It Is</div>
  </div>
  <div class="website">www.velmora.com</div>
</section>

<section class="card card--back">
  <div class="brand">
    <div class="brand__name">Velmora</div>
    <div class="brand__tagline">Always Know Where It Is</div>
  </div>

  <div class="social" aria-label="Social channels">
    <span class="social__tile"></span>
    <span class="social__tile"></span>
    <span class="social__tile"></span>
  </div>

  <div class="divider"></div>

  <div class="person">
    <div class="person__name">Harold B Pennick</div>
    <div class="person__role">Owner</div>
  </div>

  <ul class="contacts">
    <li class="contacts__item">
      <span class="contacts__icon">
        <svg viewBox="0 0 24 24"><path fill="#fff" d="M6.6 10.8a15 15 0 0 0 6.6 6.6l2.2-2.2c.3-.3.7-.4 1-.2 1.1.4 2.3.6 3.6.6.6 0 1 .4 1 1V20c0 .6-.4 1-1 1A17 17 0 0 1 3 4c0-.6.4-1 1-1h3.5c.6 0 1 .4 1 1 0 1.3.2 2.5.6 3.6.1.3 0 .7-.2 1z"/></svg>
      </span>
      555-014-2286
    </li>
    <li class="contacts__item">
      <span class="contacts__icon">
        <svg viewBox="0 0 24 24"><rect x="3" y="6" width="18" height="12" fill="none" stroke="#fff" stroke-width="1.8"/><path d="M3 6l9 7 9-7" fill="none" stroke="#fff" stroke-width="1.8"/></svg>
      </span>
      hello@velmora.com
    </li>
    <li class="contacts__item">
      <span class="contacts__icon">
        <svg viewBox="0 0 24 24" fill="none" stroke="#fff" stroke-width="1.6"><circle cx="12" cy="12" r="9"/><ellipse cx="12" cy="12" rx="4" ry="9"/><path d="M3 12h18M5 7h14M5 17h14"/></svg>
      </span>
      www.velmora.com
    </li>
  </ul>

  <div class="address">your address 2nd street<br>London, USA</div>
</section>

</body>
</html>
```